Out of town New Masters of Accounting

size of ad is 7” x 9.6”
please leave one inch on bottom for footer
We want to attract out of town students to join this master's in accounting program.
You DO NOT  have to use a picture of a person.
But if you do, it should be a  male with a white shirt and should not have long hair.(look like a young executive)
THE TEXT OF THE AD IS IN THE ATTACHMENTS
THE CAP LETTERS ARE THE INSTRUCTIONS

The age we are trying to attract is from 20-30 of ages.
- a clear ad .. the text should not take up the entire ad.. it should not be very crowded -
it should be an attractive ad that people would want to see and stand out
- the text very big and take up the entire ad

```html
<!DOCTYPE html>
<html lang="en">
<head>
<meta charset="UTF-8">
<title>Remote Master of Science in Accounting</title>
<link href="https://fonts.googleapis.com/css2?family=Montserrat:wght@300;400;500;600;700;800&display=swap" rel="stylesheet">
<style>
  :root {
    --navy: #0d3a78;
    --navy-deep: #082a5c;
    --blue: #0a7ef0;
    --teal: #0fc79a;
    --panel: #1c232d;
    --white: #ffffff;
  }
  * { margin: 0; padding: 0; box-sizing: border-box; }
  html, body { width: 875px; height: 1200px; overflow: hidden; }
  body { font-family: 'Montserrat', sans-serif; background: var(--navy); }
  .ad {
    position: relative; width: 875px; height: 1200px; overflow: hidden;
    background: linear-gradient(160deg, #245296 0%, #11458c 35%, #0b3a7c 70%, #0d468f 100%);
  }
  .city-backdrop {
    position: absolute; inset: 0;
    background:
      linear-gradient(120deg, rgba(90,140,200,0.25) 0%, rgba(10,50,110,0) 40%),
      linear-gradient(60deg, rgba(10,40,100,0) 50%, rgba(80,130,190,0.22) 100%);
  }
  .hero-photo { position: absolute; left: 0; top: 0; width: 875px; height: 360px; }
  .ranking-badge {
    position: absolute; left: 644px; top: 139px; width: 208px; height: 208px;
    border-radius: 50%; background: var(--white);
  }
  .headline-new {
    position: absolute; left: 22px; top: 364px;
    font-size: 69px; font-weight: 700; color: var(--white); letter-spacing: -1px;
    text-shadow: 2px 3px 4px rgba(0,0,0,0.35); line-height: 1; white-space: nowrap;
  }
  .subhead {
    position: absolute; left: 25px; top: 452px;
    font-size: 31px; font-weight: 600; color: var(--white); letter-spacing: -0.6px;
    text-shadow: 1px 2px 3px rgba(0,0,0,0.35); white-space: nowrap;
  }
  .feature-band {
    position: absolute; left: 0; height: 44px;
    background: linear-gradient(90deg, var(--blue) 0%, #0aa5d0 50%, var(--teal) 100%);
    color: var(--white); font-weight: 700; font-size: 27px; line-height: 44px; white-space: nowrap;
  }
  .band-prices { top: 509px; width: 407px; padding-left: 96px; }
  .band-date { top: 591px; width: 536px; padding-left: 178px; }
  .band-icon { position: absolute; }
  .icon-price { left: 24px; top: 503px; width: 66px; height: 64px; }
  .icon-calendar { left: 88px; top: 572px; width: 67px; height: 72px; }
  .career-pitch {
    position: absolute; left: 53px; top: 668px;
    font-size: 34px; font-weight: 800; line-height: 45px; letter-spacing: 0; white-space: nowrap;
    background: linear-gradient(90deg, var(--blue) 0%, #0aa0d4 55%, var(--teal) 100%);
    -webkit-background-clip: text; background-clip: text; color: transparent;
    filter: drop-shadow(1px 2px 2px rgba(0,0,0,0.35));
  }
  .details-panel {
    position: absolute; left: 0; top: 780px; width: 875px; height: 302px;
    background: linear-gradient(90deg, var(--panel) 0%, #1d2632 55%, #123a6e 85%, #0f3f80 100%);
  }
  .details-text {
    position: absolute; left: 25px; top: 14px;
    color: var(--white); font-size: 21px; font-weight: 500; line-height: 35.3px; white-space: nowrap;
  }
  .details-text .placement-title { font-weight: 600; text-decoration: underline; text-underline-offset: 3px; }
  .benefit-list { list-style: none; }
  .benefit-list li { display: flex; align-items: center; font-weight: 300; font-size: 21px; }
  .benefit-list svg { width: 34px; height: 28px; margin-right: 4px; flex-shrink: 0; }
  .duration-band {
    position: absolute; left: 188px; top: 237px; width: 499px; height: 44px;
    background: linear-gradient(90deg, var(--blue) 0%, #0aa5d0 55%, var(--teal) 100%);
    color: var(--white); font-size: 28px; font-weight: 600; line-height: 44px; text-align: center;
    letter-spacing: -0.5px; text-shadow: 1px 2px 3px rgba(0,0,0,0.4); white-space: nowrap;
  }
</style>
</head>
<body>
<main class="ad">
  <div class="city-backdrop" role="img" aria-label="Blue-toned view of glass office towers"></div>

  <svg class="hero-photo" viewBox="0 0 875 360" role="img" aria-label="Photo of a professional typing on a laptop beside a notebook and calculator">
    <defs>
      <linearGradient id="deskTone" x1="0" y1="0" x2="1" y2="1">
        <stop offset="0" stop-color="#cfd5dc"/>
        <stop offset="0.45" stop-color="#e4e6e8"/>
        <stop offset="0.75" stop-color="#c9b8a0"/>
        <stop offset="1" stop-color="#9aa4ae"/>
      </linearGradient>
      <linearGradient id="waveBlue" x1="0" y1="0" x2="1" y2="0">
        <stop offset="0" stop-color="#0a7ef0"/>
        <stop offset="1" stop-color="#0fc0b0"/>
      </linearGradient>
    </defs>
    <path d="M0 0 H875 V228 C700 280 450 325 250 322 C140 320 60 305 0 292 Z" fill="url(#deskTone)"/>
    <path d="M0 300 C80 318 160 330 260 332 C470 334 700 290 875 238" fill="none" stroke="#0b3f86" stroke-width="14"/>
    <path d="M0 316 C90 335 180 345 280 345 C480 344 700 300 875 252" fill="none" stroke="url(#waveBlue)" stroke-width="6"/>
  </svg>

  <div class="ranking-badge" role="img" aria-label="Masters ranking award badge"></div>

  <h1 class="headline-new">ALL NEW!</h1>
  <p class="subhead">REMOTE PROGRAM FOR OUT OF TOWN STUDENTS</p>

  <div class="feature-band band-prices">NEW LOWER PRICES</div>
  <svg class="band-icon icon-price" viewBox="0 0 66 64" aria-hidden="true">
    <path d="M8 2 H58 V34 H66 L33 64 L0 34 H8 Z" fill="#ffffff"/>
    <text x="33" y="40" text-anchor="middle" font-family="Montserrat, sans-serif" font-weight="700" font-size="36" fill="#0fa8c8">$</text>
  </svg>

  <div class="feature-band band-date">BEGINNING AUGUST 17</div>
  <svg class="band-icon icon-calendar" viewBox="0 0 67 72" aria-hidden="true">
    <defs>
      <linearGradient id="calFill" x1="0" y1="0" x2="1" y2="1">
        <stop offset="0" stop-color="#0a7ef0"/>
        <stop offset="1" stop-color="#0fb8b0"/>
      </linearGradient>
    </defs>
    <rect x="3" y="10" width="61" height="59" rx="4" fill="url(#calFill)" stroke="#ffffff" stroke-width="5"/>
    <rect x="3" y="10" width="61" height="14" fill="#ffffff"/>
    <rect x="15" y="1" width="7" height="18" rx="3" fill="#ffffff"/>
    <rect x="45" y="1" width="7" height="18" rx="3" fill="#ffffff"/>
    <path d="M18 46 L29 56 L50 35" fill="none" stroke="#ffffff" stroke-width="6" stroke-linecap="round" stroke-linejoin="round"/>
  </svg>

  <h2 class="career-pitch">ADVANCE FURTHER IN YOUR CAREER WITH<br>A MASTERS OF SCIENCE IN ACCOUNTING</h2>

  <section class="details-panel">
    <div class="details-text">
      <p>Northvale - Halbrook Crest University (HCU)</p>
      <p>Master in Accounting Program Received the highest possible star rating</p>
      <p class="placement-title">CPN/Meridian Alliance Job Placement Advantage :</p>
      <ul class="benefit-list">
        <li><svg viewBox="0 0 34 28" aria-hidden="true"><path d="M2 15 L12 25 L32 3" fill="none" stroke="#12b4d0" stroke-width="6" stroke-linejoin="round"/></svg>96% placement rate</li>
        <li><svg viewBox="0 0 34 28" aria-hidden="true"><path d="M2 15 L12 25 L32 3" fill="none" stroke="#12b4d0" stroke-width="6" stroke-linejoin="round"/></svg>8 placement coordinators</li>
        <li><svg viewBox="0 0 34 28" aria-hidden="true"><path d="M2 15 L12 25 L32 3" fill="none" stroke="#12b4d0" stroke-width="6" stroke-linejoin="round"/></svg>Decades of relationships with 100’s of firm</li>
      </ul>
    </div>
    <div class="duration-band">A MASTERS IN ONLY 15 MONTHS</div>
  </section>
</main>
</body>
</html>
```